Brochure Design Project A5 (UK) 64 pages apox Making Money From Financial Trading

I require a website (long sales letter) turned into a A5 booklet for mailing out will will be full colour. You must provide a complete end to end to service, I will provide all the text and photos and you need to layout and design the brochure, resize photos to fit. I see the size being around 64 sides of UK A5 paper
148 x 210mm 5.83 x 8.27

You must be creative with text layout and typography, this is very text heavy over 10,000 words in to total. the website can be seen at www.brassfold-ledger.com however this is NOT the final text but gives you an idea. (I have attached 5 pages of text)

They typical reader is male over 40, it needs to be readable, experience with magazine layouts and advantage

The finished project must be ready to go to print.

So it needs a front and back cover designed - I have attached a sample DVD cover as an idea from one of our products and then the inside pages, designed/set out
Updates

We have made the project guaranteed so step up and give me your best designs

Reason: Dear All. The standard of work submitted so far has been very poor and amateurish. We have decided to use another company for the front and back cover, therefore leaving you to concentrate on the text for inside the booklet. If you wish to resubmit some better designs then please go ahead. Thx

Target Market(s)

The typical client is Male, professional, looking make money from the stockmarket. The end user already knows the author

Industry/Entity Type

Financial

Requirements
Must have
• Must have good and creative typography

```html
<!DOCTYPE html>
<html lang="en">
<head>
<meta charset="utf-8">
<title>Brassfold Ledger – Booklet Spread 3–4</title>
<link rel="stylesheet" href="https://fonts.googleapis.com/css2?family=Anton&family=Arimo:wght@400;700&family=Tinos:wght@400;700&display=swap">
<style>
  :root {
    --ink: #111111;
    --paper: #ffffff;
    --accent: #00aeef;
    --frame: #d4d4d4;
    --rule: #222222;
    --frame-line: #3a6fd8;
  }
  * { box-sizing: border-box; margin: 0; padding: 0; }
  html, body { width: 1200px; height: 852px; overflow: hidden; background: var(--paper); }
  .spread { position: relative; width: 1200px; height: 852px; background: var(--paper); color: var(--ink); overflow: hidden; }
  .page-edge { position: absolute; top: 0; bottom: 0; width: 1px; background: var(--ink); }
  .page-edge--outer-left { left: 0; }
  .page-edge--gutter { left: 600px; }
  .page-edge--outer-right { right: 0; }
  .folio { position: absolute; top: 8px; font: 700 17px/1 Arimo, Arial, sans-serif; }
  .folio--left { left: 43px; }
  .folio--right { right: 43px; }
  .accent-band { position: absolute; top: 140px; left: 43px; width: 1116px; height: 12px; background: var(--accent); }

  .headline-box { position: absolute; left: 43px; top: 162px; width: 492px; height: 183px; border: 1px solid var(--frame-line); }
  .headline { font-family: Anton, Impact, sans-serif; font-weight: 400; text-transform: uppercase; color: var(--ink); }
  .headline__line { position: absolute; left: 8px; display: block; white-space: nowrap; line-height: 1; transform-origin: left top; }
  .headline__line--first { top: 9px; font-size: 41px; transform: scaleX(1.24); }
  .headline__line--second { top: 59px; font-size: 37px; transform: scaleX(1.11); }
  .headline__figure { top: 97px; font-size: 91px; letter-spacing: -1px; transform: scaleX(1.17); }

  .statement-frame { position: absolute; left: 43px; top: 390px; width: 492px; height: 239px; background: var(--frame); padding: 11px 14px 13px; }
  .statement { position: relative; width: 100%; height: 100%; background: var(--paper); font-family: Arimo, Arial, sans-serif; color: #333; }
  .statement__client { position: absolute; left: 22px; top: 54px; font-size: 10px; }
  .statement__meta { position: absolute; right: 20px; top: 36px; text-align: right; font-size: 9.5px; line-height: 11.5px; font-weight: 700; }
  .statement__meta .title { font-size: 11px; }
  .statement__summary { position: absolute; left: 22px; right: 20px; top: 124px; font-size: 8.5px; }
  .statement__summary h3 { font-size: 10px; font-weight: 700; border-bottom: 1px solid var(--rule); padding-bottom: 2px; }
  .statement__summary table { width: 100%; border-collapse: collapse; }
  .statement__summary th { text-align: left; font-weight: 700; padding: 3px 0; border-bottom: 1px solid var(--rule); }
  .statement__summary td { padding: 1.5px 0; }
  .statement__summary .num { text-align: right; }
  .statement__summary .gap td { padding-top: 10px; border-top: 1px solid #888; }

  .body-copy { font-family: Tinos, "Times New Roman", serif; font-size: 17.2px; line-height: 23.6px; text-align: justify; }
  .body-copy p + p { margin-top: 23.6px; }
  .intro-copy { position: absolute; left: 43px; top: 652px; width: 490px; }
  .section-head { position: absolute; left: 43px; top: 788px; font: 700 22px/1 Arimo, Arial, sans-serif; color: var(--accent); letter-spacing: 0.2px; }

  .letter-columns { position: absolute; left: 664px; top: 158px; width: 496px; height: 694px; column-count: 2; column-gap: 32px; column-fill: auto; overflow: hidden; }
</style>
</head>
<body>
<main class="spread">
  <span class="page-edge page-edge--outer-left"></span>
  <span class="page-edge page-edge--gutter"></span>
  <span class="page-edge page-edge--outer-right"></span>
  <span class="folio folio--left">3</span>
  <span class="folio folio--right">4</span>
  <div class="accent-band"></div>

  <section class="headline-box">
    <h1 class="headline">
      <span class="headline__line headline__line--first">It was also the month</span>
      <span class="headline__line headline__line--second">I banked a tax-free profit of</span>
      <span class="headline__line headline__figure">£314,377.81</span>
    </h1>
  </section>

  <figure class="statement-frame">
    <div class="statement">
      <div class="statement__client">R J Hallworth Esq</div>
      <div class="statement__meta">
        <div class="title">STATEMENT</div>
        <div>23 SEP 2008</div>
        <div>Account No. 5****</div>
        <div>Printed at 02:42:36</div>
        <div>Page 1</div>
      </div>
      <div class="statement__summary">
        <h3>ACCOUNT SUMMARY IN STERLING</h3>
        <table>
          <tr><th>Details</th><th class="num">Total £</th></tr>
          <tr><td>CASH BALANCE</td><td class="num">183,949.61</td></tr>
          <tr><td>RUNNING PROFIT OR LOSS</td><td class="num">130,928.06</td></tr>
          <tr><td>TOTAL SURPLUS OR DEFICIT</td><td class="num">314,877.81</td></tr>
          <tr class="gap"><td>DEPOSIT INCURRED ON OPEN POSITIONS</td><td class="num">169,545.36</td></tr>
        </table>
      </div>
    </div>
  </figure>

  <div class="body-copy intro-copy">
    <p>So don’t believe the doom and gloom headlines; there is always a winner and a loser in financial markets and should you become part of my program, you can be part of the small but elite group that profits from opportunities like this. Of course I also make plenty from markets moving up as well.</p>
  </div>
  <h2 class="section-head">THIS IS ABOUT YOU NOT ME</h2>

  <article class="body-copy letter-columns">
    <p>What I show you in this letter is not to boast or impress you, but to give you an idea of what is possible. This letter is not about me, it’s about YOU and how you can build up your own fortune, and more importantly, financial freedom. As impressive as making £24,900 a week may sound, it’s not the money that was ever important to me - it was getting the FREEDOM.</p>
    <p>As the old saying goes, “you don’t want to buy a hair growth tonic from a bald man” – and you don’t want to learn to trade and invest in financial markets from someone who has not achieved self-made multi millionaire status.</p>
    <p>I have been in this business for over 26 years and have been featured favourably and quoted in over 200 newspapers, media outlets and websites including BNTV, Kestrel Finance, Tradewatcher, Wirepost.com, Courier, Sunday Courier, Onlooker, Sentinel, The Chronicle, Sunday Chronicle, Daily Bulletin, Which Holdings, Rising Company Investor, Hudson Times, Hornsandclaws, Square Mile Monthly, Docklands Review, Institutional Allocator Asia and Equity Notes Magazine, just to name a few.</p>
    <p>My Clipstream video clip channel has been watched by over 465,000+ worldwide viewers. For videos on finance, this is a large number and I don’t even promote my channel.</p>
    <p>My point is that I have not just crawled from under a rock. I am not some “here today, gone tomorrow”, quick-buck merchant.</p>
    <p>The program which I am inviting to you to be part of started in 2007 and has made money every year, through what many say has been the hardest trading years in recent history.</p>
    <p>You can see video clips of my current members and what they have to say. Prior to 2007, I have taught men and women from all over the globe and my personal</p>
  </article>
</main>
</body>
</html>
```